Brisk Nova residential and commercial cleaning

We need a Business card design for a new residential and commercial cleaning company based in UAE- Abu Dhabi named (BRISK NOVA)
we provide a residential cleaning service based in hourly rate (Maid Rent - Baby Setting), Also a commercial and offices cleaning.
Our logo is attached for your reference

Target Market(s)

Women who are 22 to 60 years old.

Industry/Entity Type

Residential

Requirements
Should not have
• it should not have an old-style fonts

```html
<!DOCTYPE html>
<html lang="en">
<head>
<meta charset="utf-8">
<title>Brisk Nova – Business Card</title>
<link href="https://fonts.googleapis.com/css2?family=Roboto:wght@300;400;500;700&display=swap" rel="stylesheet">
<style>
  :root {
    --page-bg: #ece9e4;
    --card-white: #ffffff;
    --brand-blue: #1e8fce;
    --deep-blue: #1571b4;
    --fresh-green: #9ccd3c;
    --text-dark: #2a2a2a;
    --text-muted: #9a9a9a;
  }
  html, body {
    margin: 0;
    padding: 0;
    width: 1200px;
    height: 1023px;
    overflow: hidden;
    background: var(--page-bg);
    font-family: "Roboto", Arial, sans-serif;
  }
  .business-card {
    position: absolute;
    left: 145px;
    top: 251px;
    width: 910px;
    height: 520px;
    border-radius: 6px;
    overflow: hidden;
    box-shadow: 0 18px 40px rgba(0,0,0,0.22);
  }
  .card-bands {
    position: absolute;
    inset: 0;
  }
  .brand-block {
    position: absolute;
    left: 0;
    right: 0;
    top: 52px;
    text-align: center;
  }
  .brand-name {
    font-weight: 700;
    font-size: 68px;
    line-height: 1;
    color: var(--brand-blue);
  }
  .brand-tagline {
    margin-top: 16px;
    font-weight: 300;
    font-size: 25px;
    letter-spacing: 3px;
    color: var(--text-muted);
  }
  .holder {
    position: absolute;
    left: 0;
    right: 0;
    top: 252px;
    text-align: center;
    font-size: 30px;
    color: var(--text-dark);
  }
  .holder-name { font-weight: 700; }
  .holder-role { font-weight: 400; font-size: 24px; }
  .contact-list {
    position: absolute;
    left: 0;
    right: 0;
    top: 322px;
    margin: 0;
    padding: 0;
    list-style: none;
    text-align: center;
    font-size: 25px;
    line-height: 40px;
    color: var(--text-dark);
  }
  .contact-label { font-weight: 700; }
</style>
</head>
<body>
  <div class="business-card">
    <svg class="card-bands" width="910" height="520" viewBox="0 0 910 520" aria-hidden="true">
      <defs>
        <linearGradient id="whiteFace" x1="0" y1="0" x2="0" y2="1">
          <stop offset="0" stop-color="#ffffff"/>
          <stop offset="1" stop-color="#f0f0f0"/>
        </linearGradient>
        <linearGradient id="greyBand" x1="0" y1="0" x2="0" y2="1">
          <stop offset="0" stop-color="#c9cacc"/>
          <stop offset="1" stop-color="#e4e5e6"/>
        </linearGradient>
        <linearGradient id="greenBand" x1="0" y1="0" x2="0" y2="1">
          <stop offset="0" stop-color="#a6d445"/>
          <stop offset="0.6" stop-color="#c6e57a"/>
          <stop offset="1" stop-color="#8cc232"/>
        </linearGradient>
        <linearGradient id="blueBand" x1="0" y1="0" x2="1" y2="0">
          <stop offset="0" stop-color="#5fb6dd"/>
          <stop offset="1" stop-color="#1571b4"/>
        </linearGradient>
      </defs>
      <rect width="910" height="520" fill="url(#whiteFace)"/>
      <rect x="0" y="228" width="910" height="6" fill="var(--brand-blue)"/>
      <rect x="0" y="240" width="910" height="62" fill="url(#greyBand)"/>
      <rect x="0" y="302" width="910" height="218" fill="url(#greenBand)"/>
      <path d="M0 478 Q 455 452 910 440 L910 520 L0 520 Z" fill="url(#blueBand)"/>
    </svg>

    <div class="brand-block">
      <div class="brand-name">Brisk Nova</div>
      <div class="brand-tagline">Residential &amp; Commercial Cleaning</div>
    </div>

    <div class="holder"><span class="holder-name">Maya Rahal</span> <span class="holder-role">| Owner</span></div>

    <ul class="contact-list">
      <li><span class="contact-label">[T]:</span> 02 555 0148</li>
      <li><span class="contact-label">[F]:</span> 02 555 0193</li>
      <li><span class="contact-label">[E]:</span> info@brisknova.com</li>
    </ul>
  </div>
</body>
</html>
```